Business Card Design

We are a manufacturing and distribution company with most of our customer base being supermarkets. We have established brand guidelines that are attached.

```html
<!DOCTYPE html>
<html lang="en">
<head>
<meta charset="UTF-8">
<title>Corvana Business Card</title>
<link href="https://fonts.googleapis.com/css2?family=Arimo:wght@400;700&display=swap" rel="stylesheet">
<style>
  :root {
    --brand-blue: #0a6bb0;
    --brand-red: #e31b23;
    --ink: #1a1a1a;
    --paper: #ffffff;
    --backdrop: #e9ecef;
  }
  * { margin: 0; padding: 0; box-sizing: border-box; }
  html, body {
    width: 1200px; height: 1000px; overflow: hidden;
    background: var(--backdrop);
    font-family: "Arimo", Arial, sans-serif;
  }
  .canvas {
    position: relative; width: 1200px; height: 1000px;
    display: flex; flex-direction: column; align-items: center; justify-content: center; gap: 28px;
  }
  .card {
    position: relative; width: 800px; height: 457px;
    border-radius: 24px; overflow: hidden;
    box-shadow: 0 6px 18px rgba(0,0,0,0.18);
  }
  /* Back side */
  .card-back {
    background: var(--brand-blue);
    display: flex; align-items: center; justify-content: center;
  }
  .brand {
    display: flex; align-items: center; gap: 18px;
  }
  .brand-mark {
    width: 34px; height: 34px; background: var(--brand-red);
  }
  .brand-name {
    font-weight: 700; letter-spacing: 4px; line-height: 1;
  }
  .card-back .brand-name { color: var(--paper); font-size: 76px; }
  /* Front side */
  .card-front { background: var(--paper); }
  .wave { position: absolute; inset: 0; width: 100%; height: 100%; }
  .front-brand {
    position: absolute; left: 48px; top: 168px;
  }
  .front-brand .brand-mark { width: 26px; height: 26px; }
  .front-brand .brand-name { color: var(--ink); font-size: 50px; letter-spacing: 3px; }
  .divider {
    position: absolute; left: 418px; top: 70px; width: 2px; height: 200px;
    background: var(--brand-red);
  }
  .contact {
    position: absolute; left: 448px; top: 78px; color: var(--ink);
  }
  .person-name {
    font-size: 30px; font-weight: 700; letter-spacing: 1px; line-height: 1.1;
  }
  .person-name .first { color: var(--brand-red); }
  .person-name .last { color: var(--brand-blue); }
  .person-title { font-size: 17px; margin-top: 4px; }
  .address { font-size: 17px; line-height: 1.3; margin-top: 16px; }
  .contact-list { list-style: none; margin-top: 14px; font-size: 17px; line-height: 1.5; }
  .contact-list li { display: flex; align-items: center; gap: 10px; }
  .contact-list svg { width: 16px; height: 16px; fill: var(--brand-blue); flex: none; }
</style>
</head>
<body>
<main class="canvas">
  <section class="card card-back" aria-label="Business card back">
    <div class="brand">
      <span class="brand-mark"></span>
      <span class="brand-name">CORVANA</span>
    </div>
  </section>

  <section class="card card-front" aria-label="Business card front">
    <svg class="wave" viewBox="0 0 800 457" preserveAspectRatio="none" aria-hidden="true">
      <path d="M0,300 C90,380 230,398 400,412 C560,424 700,420 770,457 L0,457 Z" fill="var(--brand-blue)"/>
      <path d="M190,388 C420,412 640,392 790,457 L774,457 C650,404 430,420 190,390 Z" fill="var(--brand-red)"/>
    </svg>

    <div class="brand front-brand">
      <span class="brand-mark"></span>
      <span class="brand-name">CORVANA</span>
    </div>

    <div class="divider"></div>

    <div class="contact">
      <h1 class="person-name"><span class="first">DALEN</span> <span class="last">MORROW</span></h1>
      <p class="person-title">CEO/Founder</p>
      <p class="address">2140 Kestrel Lane<br>Country Name, AB 50312</p>
      <ul class="contact-list">
        <li>
          <svg viewBox="0 0 24 24"><path d="M6.6 10.8a15.1 15.1 0 0 0 6.6 6.6l2.2-2.2a1 1 0 0 1 1-.25 11.4 11.4 0 0 0 3.6.57 1 1 0 0 1 1 1V20a1 1 0 0 1-1 1A17 17 0 0 1 3 4a1 1 0 0 1 1-1h3.5a1 1 0 0 1 1 1c0 1.25.2 2.45.57 3.57a1 1 0 0 1-.25 1z"/></svg>
          555-014-2290
        </li>
        <li>
          <svg viewBox="0 0 24 24"><path d="M2 5h20v14H2z M3.5 6.5 12 13l8.5-6.5" fill="none" stroke="var(--brand-blue)" stroke-width="2"/></svg>
          info@corvana.com.au
        </li>
        <li>
          <svg viewBox="0 0 24 24"><circle cx="12" cy="12" r="10"/><path d="M2 12h20M12 2c3 3 3 17 0 20M12 2c-3 3-3 17 0 20" fill="none" stroke="#fff" stroke-width="1.4"/></svg>
          www.corvana.com.au
        </li>
      </ul>
    </div>
  </section>
</main>
</body>
</html>
```